Design a Pre-Workout Package Design For a Supplement Company!

Create a colourful and energetic design for our pre-workout packaging! A small container that holds 30 servings of pre-workout needs to be designed to be eye-catching and inspirational! We want it to jump off the shelf into your face and scream positivity, energy and colour.

I've attached our logo- VEX Stamina which should be the face of the package with the colourful packaging behind it! Feel free to change it around! I've also attached a supplement company's pre-workout design that I love! Good luck!!!

Target Market(s)

Fitness goers

Industry/Entity Type

Fitness

Colors

Designer to choose colors to be used in the design.

Requirements
Must have
• -Logo-VEX Stamina on the front
• - Colourful, energetic, inspiration package

```html
<!DOCTYPE html>
<html lang="en">
<head>
<meta charset="utf-8">
<title>VEX Stamina Pre-Workout Label</title>
<link href="https://fonts.googleapis.com/css2?family=Exo+2:ital,wght@0,500;0,700;0,800;1,700;1,800&family=Roboto+Condensed:wght@400;700&display=swap" rel="stylesheet">
<style>
  :root {
    --canvas: #ffffff;
    --brand-blue: #2f7fd6;
    --brand-gold: #f0b323;
    --energy-orange: #f26a2e;
    --strength-pink: #e8308f;
    --ink: #1b1b1b;
    --white: #ffffff;
    --facts-yellow: #f5b820;
    --back-dark: #1f3a2c;
  }
  * { box-sizing: border-box; margin: 0; padding: 0; }
  html, body { width: 1200px; height: 675px; overflow: hidden; background: var(--canvas); }
  body { position: relative; font-family: "Exo 2", sans-serif; }

  .label { position: absolute; top: 150px; width: 440px; height: 375px; overflow: hidden; border-radius: 6px; }
  .label--front { left: 110px; }
  .label--back { left: 650px; }

  .front-art {
    position: absolute; inset: 0;
    background:
      radial-gradient(circle at 50% 45%, #ffffff 0%, rgba(255,255,255,0.85) 22%, rgba(255,255,255,0) 55%),
      radial-gradient(circle at 15% 30%, #f6a33a 0%, rgba(246,163,58,0) 40%),
      radial-gradient(circle at 85% 25%, #e95a6a 0%, rgba(233,90,106,0) 40%),
      radial-gradient(circle at 80% 85%, #8cc85a 0%, rgba(140,200,90,0) 45%),
      radial-gradient(circle at 15% 85%, #6aa8d8 0%, rgba(106,168,216,0) 45%),
      linear-gradient(135deg, #f3c35a, #d86ab0 50%, #7ccf9a);
  }
  .brand { position: absolute; left: 0; right: 0; top: 72px; text-align: center; }
  .brand__name { font-weight: 800; font-size: 68px; color: var(--brand-blue); letter-spacing: 1px; line-height: 1; }
  .brand__tag { margin-top: 10px; font-weight: 500; font-size: 17px; letter-spacing: 2px; color: var(--brand-blue); }

  .servings { position: absolute; left: 34px; top: 218px; color: var(--white); text-align: center; }
  .servings__num { font-weight: 800; font-size: 58px; line-height: 1; }
  .servings__word { font-weight: 700; font-size: 14px; letter-spacing: 2px; }

  .claims { position: absolute; left: 150px; top: 232px; font-style: italic; font-weight: 800; }
  .claims__energy { font-size: 26px; color: var(--energy-orange); }
  .claims__strength { font-size: 22px; color: var(--strength-pink); margin-top: 2px; }

  .icon-strip { position: absolute; left: 40px; right: 40px; bottom: 22px; height: 44px; border-radius: 8px;
    background: linear-gradient(90deg, #2a2a2a, #4a3a1a 50%, #2a2a2a); opacity: 0.85; }

  .back-art {
    position: absolute; inset: 0;
    background:
      radial-gradient(circle at 20% 30%, #2b5ea8 0%, rgba(43,94,168,0) 45%),
      radial-gradient(circle at 75% 25%, #b3402a 0%, rgba(179,64,42,0) 45%),
      radial-gradient(circle at 85% 80%, #7a9a2a 0%, rgba(122,154,42,0) 45%),
      linear-gradient(135deg, #1c3f5a, var(--back-dark) 55%, #3a2a1a);
  }
  .directions { position: absolute; left: 18px; top: 30px; width: 100px; color: var(--white);
    font-family: "Roboto Condensed", sans-serif; font-size: 10px; line-height: 1.35; }
  .directions p + p { margin-top: 10px; }

  .facts { position: absolute; left: 135px; top: 28px; width: 285px; background: var(--facts-yellow);
    color: var(--ink); font-family: "Roboto Condensed", sans-serif; padding: 8px 10px; }
  .facts__title { font-family: "Exo 2", sans-serif; font-weight: 800; font-size: 22px; line-height: 1; }
  .facts__meta { font-size: 11px; line-height: 1.25; margin-top: 3px; border-bottom: 5px solid var(--ink); padding-bottom: 2px; }
  .facts table { width: 100%; border-collapse: collapse; font-size: 10px; }
  .facts th { font-size: 8px; text-align: left; border-bottom: 1px solid var(--ink); }
  .facts th.dv { text-align: right; }
  .facts td { border-bottom: 1px solid rgba(0,0,0,0.5); padding: 1px 0; }
  .facts td.amt { text-align: right; padding-right: 10px; }
  .facts td.dv { text-align: right; width: 36px; }
  .facts tr.rule td { border-bottom: 3px solid var(--ink); }
  .facts__foot { font-size: 8px; line-height: 1.25; margin-top: 3px; }
  .facts__foot strong { font-weight: 700; }

  .storage { position: absolute; left: 135px; right: 20px; bottom: 22px; color: var(--white);
    font-family: "Roboto Condensed", sans-serif; font-size: 11px; line-height: 1.3; }
</style>
</head>
<body>
  <section class="label label--front" aria-label="Front label">
    <div class="front-art" role="img" aria-label="Colourful burst of energy light streaks in orange, pink, green and blue"></div>
    <div class="brand">
      <div class="brand__name">VEX Stamina</div>
      <div class="brand__tag">PRE-WORKOUT SUPPLEMENT</div>
    </div>
    <div class="servings">
      <div class="servings__num">30</div>
      <div class="servings__word">SERVINGS</div>
    </div>
    <div class="claims">
      <div class="claims__energy">EXPLOSIVE ENERGY</div>
      <div class="claims__strength">INCREDIBLE STRENGTH</div>
    </div>
    <div class="icon-strip" role="img" aria-label="Row of benefit icons: muscle, speaker, bomb, drink and flame"></div>
  </section>

  <section class="label label--back" aria-label="Back label">
    <div class="back-art" role="img" aria-label="Dark multicolour energy background with red and green streaks"></div>
    <div class="directions">
      <p>Fuel every session with clean power. Our blend helps you push harder, stay focused and recover faster.</p>
      <p>Directions: Mix one scoop with water before training. Do not exceed two servings per day. Consult a physician before use.</p>
    </div>
    <div class="facts">
      <div class="facts__title">Supplement Facts</div>
      <div class="facts__meta">Serving Size 7g<br>Servings Per Container 30</div>
      <table>
        <tr><th>Amount Per Serving</th><th></th><th class="dv">% Daily Value*</th></tr>
        <tr><td>Calories</td><td class="amt">5</td><td class="dv">&lt; 1%</td></tr>
        <tr><td>Total Carbohydrate</td><td class="amt">1g</td><td class="dv">4%</td></tr>
        <tr class="rule"><td>Calcium</td><td class="amt">36mg</td><td class="dv">**</td></tr>
        <tr><td>L-Citrulline-Malate</td><td class="amt">2000mg</td><td class="dv">**</td></tr>
        <tr><td>Agmatine Sulfate</td><td class="amt">250mg</td><td class="dv">**</td></tr>
        <tr><td>Caffeine</td><td class="amt">300mg</td><td class="dv">**</td></tr>
        <tr><td>Di Caffeine Malate</td><td class="amt">50mg</td><td class="dv">**</td></tr>
        <tr><td>L Hordenine HCL</td><td class="amt">50mg</td><td class="dv">**</td></tr>
        <tr><td>PiperLean®<br>&nbsp;Black Pepper Extract</td><td class="amt">2mg</td><td class="dv">**</td></tr>
        <tr class="rule"><td>Yohimbine HCL</td><td class="amt">3mg</td><td class="dv">**</td></tr>
      </table>
      <div class="facts__foot">*Percent Daily Values are based on a 2,000 calorie diet.<br>**Daily Value not established.<br><strong>Other Ingredients:</strong> (Soluble Corn Fiber), Natural and Artificial Flavors, Citric Acid, Silicon Dioxide, Malic Acid, Sucralose, Calcium Carbonate.</div>
    </div>
    <p class="storage">Store in a cool or dry place below 30 °C. Do not expose to excessive heat or moisture</p>
  </section>
</body>
</html>
```